Redcliff Oil & Gas Exploration, LLC

Our website (www.redcliffoilandgas.example) is poorly done and dated. I want to redo it with one main page and wide format photos or oil & gas drilling and production. Perhaps all of the pages listed on the left side of the existing site could be viewed by scrolling down further on the new main page. I want something clean and easy to navigate.

Target Market(s)

Other oil and gas companies and people that we have contacted regarding selling or leasing their mineral rights. These people will come to our website to research our company and become more comfortable doing business with us.

Industry/Entity Type

Oil And Gas

Coding

Coded - Design and coding required

Number of Pages Required

1 page

Font styles to use
Serif

Requirements
Must have
• Clean and uncluttered. Nice, clear wide format picture or oil well or rig and landscape.

```html
<!DOCTYPE html>
<html lang="en">
<head>
<meta charset="utf-8">
<title>Redcliff Oil &amp; Gas Exploration, LLC</title>
<link rel="stylesheet" href="https://fonts.googleapis.com/css2?family=Ubuntu:wght@400;500;700&display=swap">
<style>
:root{
  --yellow:#fbb91a;
  --orange:#f0622a;
  --ink:#1f1f1f;
  --text:#3a3a3a;
  --muted:#9a9a9a;
  --white:#ffffff;
  --rule:#e3c9a6;
}
*{box-sizing:border-box;margin:0;padding:0}
html,body{width:1200px;height:2397px;overflow:hidden;background:var(--white)}
body{position:relative;font-family:"Ubuntu",sans-serif;color:var(--text)}
.abs{position:absolute}

/* header */
.brand-box{left:118px;top:16px;width:101px;height:102px;background:var(--yellow);display:flex;flex-direction:column;align-items:center;justify-content:center;gap:6px;z-index:2}
.brand-box .dot{width:34px;height:34px;border-radius:50%;background:var(--orange)}
.brand-box .name{font-size:15px;font-weight:700;color:var(--ink)}
.nav{left:251px;top:34px;display:flex;gap:24px;font-size:12px}
.nav a{color:var(--muted);text-decoration:none;padding-bottom:16px}
.nav a.active{color:var(--ink);font-weight:500;border-bottom:2px solid var(--yellow)}
.contact-mail{left:872px;top:35px;display:flex;align-items:center;gap:7px;font-size:8px;color:var(--ink);white-space:nowrap}
.contact-divider{left:1052px;top:28px;width:1px;height:28px;background:#ddd}
.contact-phone{left:1064px;top:33px}

/* photo areas */
.hero{left:88px;top:67px;width:1024px;height:449px;background:
  radial-gradient(ellipse 30% 60% at 72% 55%,rgba(220,230,240,.55),transparent 70%),
  radial-gradient(ellipse 22% 70% at 38% 60%,rgba(170,180,190,.6),transparent 70%),
  linear-gradient(180deg,#1f6fc8 0%,#5b9fe0 30%,#a9cdef 50%,#7f97b0 68%,#4e6a88 85%,#3d4f63 100%)}
.arrow{top:268px;width:49px;height:47px;background:var(--yellow);display:flex;align-items:center;justify-content:center}
.arrow.prev{left:117px}.arrow.next{left:1034px}

.about{left:88px;top:551px;width:660px;height:248px;background:var(--yellow);padding:64px 48px 0}
.about h1{font-size:18px;font-weight:500;color:var(--ink);margin-bottom:12px}
.about p{font-size:12px;line-height:19px;color:#3d2f10;max-width:500px}
.photo-flare{left:778px;top:551px;width:334px;height:499px;background:
  radial-gradient(ellipse 45% 16% at 52% 37%,#ffd23a 0%,#f28a1e 45%,rgba(214,80,30,.6) 75%,transparent 100%),
  linear-gradient(180deg,#4a3a4e 0%,#7b4d5c 18%,#b06a60 38%,#d9a07e 60%,#e9cdb4 80%,#efe4d6 100%)}
.photo-pump{left:88px;top:831px;width:316px;height:219px;background:
  radial-gradient(circle at 62% 62%,#fbe1b0 0%,#e0a45e 18%,transparent 45%),
  linear-gradient(180deg,#9c6434 0%,#b47a42 45%,#6b3f1d 78%,#2a180b 100%)}
.photo-rig{left:431px;top:831px;width:317px;height:219px;background:
  radial-gradient(ellipse 18% 30% at 62% 52%,rgba(60,60,60,.55),transparent 70%),
  linear-gradient(180deg,#3f86cf 0%,#9cc4e8 28%,#e8f0f8 45%,#6c9cc8 62%,#254f7e 75%,#1b2f46 90%,#c9a940 100%)}

/* team */
.member{top:1083px;width:292px}
.member .avatar{width:82px;height:82px;background:var(--yellow);display:flex;align-items:flex-end;justify-content:center;overflow:hidden}
.member h2{font-size:17px;font-weight:700;color:var(--ink);margin:22px 0 10px}
.member p{font-size:12px;line-height:19px;color:var(--text)}
.team-rule{top:1083px;width:1px;height:291px;background:var(--rule)}

/* history */
.history-intro{left:88px;top:1417px;width:265px;height:274px;background:var(--yellow);padding:46px 34px 0 46px}
.history-intro h2{font-size:18px;font-weight:700;color:var(--ink);margin-bottom:14px}
.history-intro p,.history-more p{font-size:12px;line-height:19px}
.history-intro p{color:#3d2f10}
.history-more{left:353px;top:1417px;width:262px;height:274px;background:var(--orange);padding:82px 34px 0 34px}
.history-more p{color:var(--white)}
.photo-night{left:615px;top:1417px;width:497px;height:274px;background:
  radial-gradient(ellipse 35% 30% at 55% 78%,rgba(150,200,255,.55),transparent 70%),
  radial-gradient(circle at 14% 10%,rgba(255,230,170,.8) 0,transparent 4%),
  linear-gradient(180deg,#2e62a8 0%,#23508e 45%,#173a68 70%,#0a1322 100%)}

/* areas */
.area{top:1726px;height:131px;display:flex;flex-direction:column;align-items:center;padding-top:28px}
.area h3{font-size:18px;font-weight:400}
.area h3 b{font-weight:700}
.area small{font-size:8px;margin-top:3px}
.area .btn{margin-top:14px;width:124px;height:32px;border-radius:16px;font-size:10px;font-weight:500;display:flex;align-items:center;justify-content:center}
.area.ok{left:88px;width:497px;background:var(--orange);color:var(--white)}
.area.ok .btn{border:1.5px solid var(--white)}
.area.tx{left:615px;width:497px;background:var(--yellow);color:#4a3608}
.area.tx h3 b{color:var(--ink)}
.area.tx .btn{background:var(--ink);color:var(--white);margin-top:26px}

/* offices */
.office-pin{top:1895px}
.office-addr{top:1993px;width:190px;font-size:18px;line-height:24px;color:var(--ink);font-style:normal}
.office-addr strong{display:block;font-weight:700;font-size:17px}
.map{top:1895px;width:294px;height:243px;border:1px solid #ddd;background:
  radial-gradient(ellipse 20% 14% at 22% 8%,#cfe5c4,transparent 75%),
  radial-gradient(ellipse 40% 30% at 60% 60%,#f3efe7,transparent 70%),
  linear-gradient(135deg,#e6e1d6 0%,#efe9dc 40%,#e3ddd0 70%,#ece6da 100%)}

/* footer */
.footer-band{left:0;top:2261px;width:1200px;height:136px;background:var(--yellow)}
.tab{top:2224px;height:80px;background:var(--yellow);border-radius:32px 32px 0 0;padding:14px 0 0 22px}
.tab small{display:block;font-size:10px;font-weight:500;color:var(--ink)}
.tab h4{font-size:17px;font-weight:700;color:var(--ink)}
.tab.brand{left:88px;width:260px;padding:18px 0 0 0;text-align:center}
.tab.brand .name{font-size:30px;font-weight:700;color:var(--orange)}
.copyright{left:118px;top:2322px;font-size:9px;line-height:14px;color:#4a3608}
.contacts{top:2288px;list-style:none;font-size:11px;color:#3d2f10}
.contacts li{display:flex;align-items:center;gap:10px;height:24px}
</style>
</head>
<body>

<!-- header -->
<div class="abs brand-box"><span class="dot"></span><span class="name">Redcliff</span></div>
<nav class="abs nav">
  <a class="active">Home</a><a>About us</a><a>History</a><a>Available Prospects</a><a>Texas</a><a>Oklahoma</a><a>Contact Us</a>
</nav>
<div class="abs contact-mail">
  <svg width="22" height="16" viewBox="0 0 24 18"><rect width="24" height="18" rx="2" fill="#fbb91a"/><path d="M1 1l11 9 11-9" fill="none" stroke="#fff" stroke-width="2"/></svg>
  inquiry@redcliffoilandgas.example
</div>
<div class="abs contact-divider"></div>
<svg class="abs contact-phone" width="20" height="18" viewBox="0 0 20 18"><path d="M2 6c0-3 4-4 8-4s8 1 8 4v2h-4V6H6v2H2z" fill="#fbb91a"/><rect x="4" y="9" width="12" height="8" rx="2" fill="#fbb91a"/></svg>

<!-- hero -->
<div class="abs hero" role="img" aria-label="Wide photo of a refinery with steel towers and blue pipework under a bright blue sky"></div>
<div class="abs arrow prev"><svg width="12" height="20" viewBox="0 0 12 20"><path d="M10 2L2 10l8 8" fill="none" stroke="#222" stroke-width="2"/></svg></div>
<div class="abs arrow next"><svg width="12" height="20" viewBox="0 0 12 20"><path d="M2 2l8 8-8 8" fill="none" stroke="#222" stroke-width="2"/></svg></div>

<!-- about -->
<section class="abs about">
  <h1>Redcliff Oil &amp; Gas Exploration, LLC</h1>
  <p>Redcliff is actively leasing and purchasing mineral rights in Texas, Oklahoma and Kansas. In Texas our area of focus is the East Texas Basin. In Oklahoma we are active across the state with emphasis on the SCOOP and the Mississippian Plays. Redcliff is dedicated to expanding our asset base, targeting oil prone plays, and continuing to acquire minerals and prospective leasehold.</p>
</section>
<div class="abs photo-flare" role="img" aria-label="Gas flare burning atop a tall stack against a hazy pink sky"></div>
<div class="abs photo-pump" role="img" aria-label="Pumpjacks silhouetted against a sepia sunset"></div>
<div class="abs photo-rig" role="img" aria-label="Offshore drilling platform on open sea under a blue sky"></div>

<!-- team -->
<article class="abs member" style="left:88px">
  <div class="avatar"><svg width="60" height="66" viewBox="0 0 60 66"><circle cx="30" cy="22" r="14" fill="#f0622a"/><path d="M2 66c0-18 12-28 28-28s28 10 28 28z" fill="#f0622a"/></svg></div>
  <h2>Charles Hadley</h2>
  <p>Charlie has over 35 years of experience as a petroleum geologist. He was most recently the East Texas Exploration Manager at Calder Energy for the past nine years. He left Calder in April 2012 to join Redcliff. Charlie's focus at Redcliff is prospecting in East Texas. Charlie attended Blue Ridge State University and the University of Delta Valley where he received a Bachelor's and Master's degree in geology.</p>
</article>
<div class="abs team-rule" style="left:417px"></div>
<article class="abs member" style="left:433px">
  <div class="avatar"><svg width="60" height="66" viewBox="0 0 60 66"><circle cx="30" cy="22" r="14" fill="#f0622a"/><path d="M2 66c0-18 12-28 28-28s28 10 28 28z" fill="#f0622a"/></svg></div>
  <h2>David Hadley</h2>
  <p>David spent seven years at Calder Energy, managing commercial real estate transactions. He left in January of 2012 to join Kevin in expanding Redcliff. He has since managed and sold several East Texas prospects. David oversees leasing prospects in East Texas. David received his Bachelor's degree in Management from Bayou State University.</p>
</article>
<div class="abs team-rule" style="left:764px"></div>
<article class="abs member" style="left:778px">
  <div class="avatar"><svg width="60" height="66" viewBox="0 0 60 66"><circle cx="30" cy="22" r="14" fill="#f0622a"/><path d="M2 66c0-18 12-28 28-28s28 10 28 28z" fill="#f0622a"/></svg></div>
  <h2>Kevin Hadley</h2>
  <p>Kevin has been an independent landman since 2005. Since starting Redcliff, he has successfully put together and sold multiple lease packages in the Haynesville, Woodford, and Niobrara plays, among many others. His current focus is purchasing minerals in Oklahoma, particularly in the SCOOP and Mississippian plays.</p>
</article>

<!-- history -->
<section class="abs history-intro">
  <h2>History</h2>
  <p><b>Redcliff</b> Oil &amp; Gas Exploration, LLC was founded in 2011 by Kevin Hadley. In 2012 David Hadley &amp; Charles Hadley joined the company. Redcliff has expanded their business, and currently has offices located in Fort Worth and <b>Oklahoma City.</b></p>
</section>
<section class="abs history-more">
  <p>Since 2012 Redcliff has acquired more than <b>25,000</b> net acres of leasehold in Texas, Oklahoma and Kansas. During the same time, the company has also purchased several thousand mineral acres in areas of active drilling. In addition, <b>Redcliff</b> has participated in dozens of wells with top tier operators.</p>
</section>
<div class="abs photo-night" role="img" aria-label="Refinery lit up at night under a deep blue sky"></div>

<!-- areas -->
<div class="abs area ok"><h3>Areas of Activity - <b>Oklahoma</b></h3><small>East Texas Basin</small><span class="btn">IMAGE MAP</span></div>
<div class="abs area tx"><h3>Areas of Activity - <b>Texas</b></h3><span class="btn">IMAGE MAP</span></div>

<!-- offices -->
<svg class="abs office-pin" style="left:90px" width="36" height="52" viewBox="0 0 36 52"><path d="M18 0C8 0 0 8 0 18c0 13 18 34 18 34s18-21 18-34C36 8 28 0 18 0z" fill="#fbb91a"/><circle cx="18" cy="17" r="7" fill="#fff"/></svg>
<address class="abs office-addr" style="left:88px"><strong>Fort Worth Office</strong>840 Commerce Street<br>Suite 310<br>Fort Worth, Texas<br>76102</address>
<div class="abs map" style="left:291px" role="img" aria-label="Street map of downtown Fort Worth marking the office"></div>

<svg class="abs office-pin" style="left:617px" width="36" height="52" viewBox="0 0 36 52"><path d="M18 0C8 0 0 8 0 18c0 13 18 34 18 34s18-21 18-34C36 8 28 0 18 0z" fill="#f0622a"/><circle cx="18" cy="17" r="7" fill="#fff"/></svg>
<address class="abs office-addr" style="left:615px"><strong>Oklahoma City<br>Office</strong>210 Elm Avenue<br>Suite 4B<br>Oklahoma City,</address>
<div class="abs map" style="left:817px" role="img" aria-label="Street map of downtown Oklahoma City marking the office"></div>

<!-- footer -->
<div class="abs footer-band"></div>
<div class="abs tab brand"><span class="name">Redcliff</span></div>
<p class="abs copyright">Content copyright 2017. All rights reserved.</p>

<div class="abs tab" style="left:369px;width:230px"><small>Land</small><h4>Oklahoma City Office</h4></div>
<ul class="abs contacts" style="left:393px">
  <li><svg width="12" height="12" viewBox="0 0 12 12"><circle cx="6" cy="3.5" r="3" fill="#222"/><path d="M0 12c0-4 3-5 6-5s6 1 6 5z" fill="#222"/></svg>Kevin Hadley</li>
  <li><svg width="12" height="12" viewBox="0 0 20 18"><path d="M2 6c0-3 4-4 8-4s8 1 8 4v2h-4V6H6v2H2z" fill="#222"/><rect x="4" y="9" width="12" height="8" rx="2" fill="#222"/></svg>405.555.0142</li>
  <li><svg width="12" height="10" viewBox="0 0 12 10"><rect width="12" height="10" fill="#222"/><path d="M0 0l6 5 6-5" fill="none" stroke="#fbb91a"/></svg>kevin@redcliffoilandgas.example</li>
</ul>

<div class="abs tab" style="left:626px;width:232px;padding-top:22px"><h4>Fort Worth Office</h4></div>
<ul class="abs contacts" style="left:650px">
  <li><svg width="12" height="12" viewBox="0 0 12 12"><circle cx="6" cy="3.5" r="3" fill="#222"/><path d="M0 12c0-4 3-5 6-5s6 1 6 5z" fill="#222"/></svg>David Hadley</li>
  <li><svg width="12" height="12" viewBox="0 0 12 12"><circle cx="6" cy="3.5" r="3" fill="#222"/><path d="M0 12c0-4 3-5 6-5s6 1 6 5z" fill="#222"/></svg>David Hadley</li>
  <li><svg width="12" height="10" viewBox="0 0 12 10"><rect width="12" height="10" fill="#222"/><path d="M0 0l6 5 6-5" fill="none" stroke="#fbb91a"/></svg>david@redcliffoilandgas.example</li>
</ul>

<div class="abs tab" style="left:882px;width:230px"><small>Geology</small><h4>Fort Worth Office</h4></div>
<ul class="abs contacts" style="left:906px">
  <li><svg width="12" height="12" viewBox="0 0 12 12"><circle cx="6" cy="3.5" r="3" fill="#222"/><path d="M0 12c0-4 3-5 6-5s6 1 6 5z" fill="#222"/></svg>Charles Hadley</li>
  <li><svg width="12" height="12" viewBox="0 0 20 18"><path d="M2 6c0-3 4-4 8-4s8 1 8 4v2h-4V6H6v2H2z" fill="#222"/><rect x="4" y="9" width="12" height="8" rx="2" fill="#222"/></svg>817.555.0187</li>
  <li><svg width="12" height="10" viewBox="0 0 12 10"><rect width="12" height="10" fill="#222"/><path d="M0 0l6 5 6-5" fill="none" stroke="#fbb91a"/></svg>charles@redcliffoilandgas.example</li>
</ul>

</body>
</html>
```